out of the box Business Card Design for a Manufacturer / Distributor

We are a manufarturer and distributor of products.
the company name is VORTANI (Pic attached)

the picture is NOT a must have on the business Card.

the Business Card should look really professional and/or special, so out of the box thinking is welcome.

there should be 2 Adresses on the Business Card for Main and Branch Office.
Email Adress, homepage, Name is required
NO Phone Number

Our working field:
Private Labeling
high Quality Production
direct distribution
warehousing
trademark registration
legal support

Main Office:
Kornblumenweg 14
08352 Lindenfeld
Germany

Branch Office:
Daska Lane
Noorabad
Pakistan

Names:
Lukas Feldhaus (Owner)
Imran Qureshi (Owner)

Email:
lukas@vortani-example.com
imran@vortani-example.com

homepage:
vortani-example.com

Industry/Entity Type

Manufacturer Distributer

Contact Information for Business Card

Vortani

Requirements
Must have
• Names, both office Adresses, email, homepage
Should not have
• Phone Number

```html
<!DOCTYPE html>
<html lang="en">
<head>
<meta charset="utf-8">
<title>Vortani Business Card</title>
<link rel="stylesheet" href="https://fonts.googleapis.com/css2?family=Lato:wght@400&family=Inter:wght@400;600&display=swap">
<style>
  :root {
    --page-bg: #e4e4e2;
    --card-bg: #c3c4bc;
    --ink: #111111;
  }
  * { margin: 0; padding: 0; box-sizing: border-box; }
  html, body {
    width: 840px;
    height: 1200px;
    overflow: hidden;
    background: var(--page-bg);
  }
  .canvas {
    position: relative;
    width: 840px;
    height: 1200px;
  }
  .card {
    position: absolute;
    left: 101px;
    width: 666px;
    height: 416px;
    background: var(--card-bg);
    color: var(--ink);
  }
  .card--front { top: 120px; }
  .card--back { top: 664px; }

  .wordmark {
    position: absolute;
    font-family: "Lato", sans-serif;
    font-weight: 400;
    letter-spacing: 0.01em;
    line-height: 1;
    color: var(--ink);
  }
  .card--front .wordmark {
    left: 58px;
    top: 80px;
    font-size: 29px;
  }
  .brand-dot {
    position: absolute;
    border-radius: 50%;
    background: var(--ink);
  }
  .card--front .brand-dot {
    left: 396px;
    top: 112px;
    width: 190px;
    height: 190px;
  }

  .back-brand {
    position: absolute;
    left: 60px;
    top: 62px;
    display: flex;
    align-items: center;
    gap: 12px;
  }
  .back-brand .wordmark {
    position: static;
    font-size: 29px;
  }
  .back-brand .brand-dot {
    position: static;
    width: 22px;
    height: 22px;
  }

  .website {
    position: absolute;
    left: 596px;
    top: 248px;
    transform-origin: 0 0;
    transform: rotate(-90deg);
    font-family: "Inter", sans-serif;
    font-size: 12px;
    letter-spacing: 0.02em;
    white-space: nowrap;
  }

  .contacts {
    position: absolute;
    left: 60px;
    top: 276px;
    display: flex;
    font-family: "Inter", sans-serif;
  }
  .person { width: 200px; }
  .person__name {
    font-weight: 600;
    font-size: 13.5px;
    line-height: 18px;
  }
  .person__email {
    font-weight: 400;
    font-size: 12.5px;
    line-height: 18px;
    margin-top: 4px;
  }

  .offices {
    position: absolute;
    left: 60px;
    top: 326px;
    font-family: "Inter", sans-serif;
    font-size: 12.5px;
    line-height: 21px;
    white-space: nowrap;
  }
  .office__label { font-weight: 600; }
</style>
</head>
<body>
<main class="canvas">
  <section class="card card--front">
    <div class="wordmark">VORTANI</div>
    <div class="brand-dot"></div>
  </section>

  <section class="card card--back">
    <div class="back-brand">
      <div class="wordmark">VORTANI</div>
      <div class="brand-dot"></div>
    </div>

    <div class="website">vortani-example.com</div>

    <div class="contacts">
      <div class="person">
        <p class="person__name">Lukas Feldhaus</p>
        <p class="person__email">lukas@vortani-example.com</p>
      </div>
      <div class="person">
        <p class="person__name">Imran Qureshi</p>
        <p class="person__email">imran@vortani-example.com</p>
      </div>
    </div>

    <div class="offices">
      <p class="office"><span class="office__label">Main office:</span> Kornblumenweg 14, 08352 Lindenfeld, Germany</p>
      <p class="office"><span class="office__label">Branch office:</span> Daska Lane, Noorabad, Pakistan</p>
    </div>
  </section>
</main>
</body>
</html>
```